Flyer-Design für landwirtschaftlichen Betrieb
Zielgruppe
Wir sind ein landwirtschaftlicher Betrieb mit Ziegenhaltung und Direktvermarktung sowie einer Hofkäserei in der wir unsere Milch zu handwerklich hergestellten Ziegenkäsen (Frischkäse, Weichkäse, Schnittkäse) verarbeiten.
Ziegenrohmilch, Wurst und Ziegenfleisch runden das Angebot ab.
Käseproben sind ebenfalls buchbar.
Im Hofladen gibt es darüber hinaus noch weitere Produkte wie Eier, Obst, Gemüse, Nudeln,...von benachbarten Betrieben.
Der Verkauf läuft über SB Automaten täglich (auch Sonn,- und Feiertage) ab 7 Uhr.
Wir sind ein moderner, gläserner Familienbetrieb und die Kunden haben jederzeit die Möglichkeit zu sehen wo ihr Lebensmittel herkommt.
Unsere Zielgruppe sind vorwiegend Familien.
Aufgabenstellung
Wir wünschen uns ein modernes Design was jedoch den landwirtschaftlichen Aspekt wiedergibt.
Das Herzstück unseres Betriebes ist die Hofkäserei.
Je nach Platzbedarf würden wir gerne eine Anfahrtsskizze auf dem Flyer haben, sowie einen Facebook Hinweis.
Unser Logo ist den Bilddateien beigefügt. Diese können gerne benutzt werden, ebenso wie Stockmaterial.

```html
<!DOCTYPE html>
<html lang="de">
<head>
<meta charset="utf-8">
<title>Ziegenhof Lindental – Flyer</title>
<link href="https://fonts.googleapis.com/css2?family=Amatic+SC:wght@700&family=Quicksand:wght@400;500;700&family=Caveat:wght@600&display=swap" rel="stylesheet">
<style>
  :root{
    --stage:#dcdcdc;
    --dark:#333334;
    --green:#1f9a4a;
    --green-light:#7bb93b;
    --mint:#d6eee0;
    --text:#3b3b3b;
    --white:#ffffff;
    --rule:#6a6a6a;
  }
  *{margin:0;padding:0;box-sizing:border-box}
  html,body{width:1200px;height:1200px;overflow:hidden;background:var(--stage)}
  .flyer{
    position:absolute;left:220px;top:42px;width:760px;height:1116px;
    background:var(--dark);overflow:hidden;font-family:"Quicksand",sans-serif;color:var(--text);
    box-shadow:0 6px 18px rgba(0,0,0,.25);
  }
  .flyer__shapes{position:absolute;inset:0}
  .headline{
    position:absolute;left:460px;width:270px;top:30px;text-align:center;color:var(--white);
    font-family:"Amatic SC",sans-serif;line-height:1;
  }
  .headline__big{font-size:62px;letter-spacing:2px}
  .headline__small{font-size:31px;letter-spacing:3px;margin-top:8px}
  .offer{position:absolute;color:var(--white);font-family:"Amatic SC",sans-serif;font-size:38px;letter-spacing:2px;line-height:1}
  .offer small{display:block;font-size:17px;letter-spacing:1px;margin-top:4px}
  .rule{position:absolute;height:1px;background:var(--rule)}
  .intro{
    position:absolute;left:35px;top:540px;width:495px;font-size:17.5px;line-height:24px;
  }
  .intro p{margin-bottom:12px}
  .intro strong{color:var(--green);font-weight:700}
  .signature{font-family:"Caveat",cursive;color:var(--green);font-size:26px;line-height:1;margin-top:-8px}
  .brand{
    position:absolute;left:259px;top:25px;width:168px;height:168px;border-radius:50%;
    background:var(--white);display:flex;align-items:center;justify-content:center;text-align:center;
    font-family:"Quicksand",sans-serif;font-weight:700;color:var(--green);font-size:22px;line-height:1.15;
  }
  .contact{position:absolute;left:252px;top:1012px;color:#d8d8d8;font-size:13.5px;line-height:20px}
  .contact div{display:flex;align-items:flex-start;gap:6px}
  .contact svg{flex:none;margin-top:4px}
  .web{position:absolute;left:40px;top:1076px;color:var(--white);font-family:"Amatic SC",sans-serif;font-size:20px;letter-spacing:1px}
  .visit{
    position:absolute;left:20px;top:983px;width:76px;height:76px;border-radius:50%;background:var(--green);
    color:var(--white);font-family:"Amatic SC",sans-serif;font-size:19px;line-height:1;text-align:center;
    display:flex;align-items:center;justify-content:center;transform:rotate(-12deg);border:2px solid var(--white);
  }
</style>
</head>
<body>
<main class="flyer">
  <svg class="flyer__shapes" width="760" height="1116" viewBox="0 0 760 1116">
    <defs>
      <linearGradient id="skyGoats" x1="0" y1="0" x2="0" y2="1">
        <stop offset="0" stop-color="#a9c8e6"/>
        <stop offset=".45" stop-color="#c9b9a6"/>
        <stop offset=".8" stop-color="#6f5a48"/>
        <stop offset="1" stop-color="#c8c1b0"/>
      </linearGradient>
      <linearGradient id="mintFade" x1="0" y1="0" x2="0" y2="1">
        <stop offset="0" stop-color="#f4faf6"/>
        <stop offset="1" stop-color="#d6eee0"/>
      </linearGradient>
      <linearGradient id="kidTones" x1="0" y1="0" x2="1" y2="1">
        <stop offset="0" stop-color="#9c7b63"/>
        <stop offset=".6" stop-color="#7a5a44"/>
        <stop offset="1" stop-color="#a47a55"/>
      </linearGradient>
    </defs>

    <path role="img" aria-label="Foto: Ziegenherde vor blauem Himmel, von unten fotografiert"
      d="M0 0 H330 C340 200 430 400 540 560 L0 560 Z" fill="url(#skyGoats)"/>

    <path d="M0 515 C110 488 240 530 360 508 C450 494 520 520 580 575 C570 680 540 760 500 830 C330 805 160 820 0 860 Z" fill="url(#mintFade)"/>

    <path role="img" aria-label="Foto: junges Zicklein lehnt auf einem Holzbalken"
      d="M590 590 C660 560 730 580 760 620 V1116 H545 C528 930 540 720 590 590 Z" fill="url(#kidTones)"/>

    <circle role="img" aria-label="Anfahrtsskizze zum Hof" cx="137" cy="937" r="103" fill="#eef2f5" stroke="#ffffff" stroke-width="3"/>
    <g transform="translate(143 916)">
      <path d="M0 -14 a10 10 0 0 1 10 10 c0 8 -10 18 -10 18 s-10 -10 -10 -18 a10 10 0 0 1 10 -10z" fill="var(--green)"/>
      <circle cx="0" cy="-4" r="4" fill="#ffffff"/>
    </g>

    <circle role="img" aria-label="Foto: Eier in Eierkartons" cx="470" cy="945" r="78" fill="#e7e2d8"/>
    <circle role="img" aria-label="Foto: angeschnittener Weichkäse" cx="352" cy="899" r="83" fill="#efe6cf" stroke="#ffffff" stroke-width="3"/>

    <circle cx="223" cy="74" r="58" fill="var(--green-light)"/>

    <line x1="465" y1="210" x2="713" y2="210" stroke="#6a6a6a"/>
    <line x1="460" y1="320" x2="713" y2="320" stroke="#6a6a6a"/>
    <line x1="495" y1="423" x2="723" y2="423" stroke="#6a6a6a"/>
    <line x1="560" y1="524" x2="723" y2="524" stroke="#6a6a6a"/>

    <g fill="var(--green)" stroke="#ffffff" stroke-width="3">
      <circle cx="408" cy="257" r="36"/>
      <circle cx="433" cy="372" r="36"/>
      <circle cx="491" cy="481" r="36"/>
      <circle cx="578" cy="568" r="36"/>
    </g>
    <g fill="none" stroke="#ffffff" stroke-width="3" stroke-linejoin="round" stroke-linecap="round">
      <path d="M396 245 h24 l-3 28 h-18 z M398 257 h20"/>
      <ellipse cx="428" cy="372" rx="13" ry="11"/>
      <circle cx="428" cy="372" r="4"/>
      <path d="M441 372 h10 m0 -5 v10"/>
      <path d="M475 490 l30 -16 v18 h-30 z M475 490 v-4"/>
      <circle cx="486" cy="485" r="2" fill="#fff"/>
      <circle cx="496" cy="482" r="2" fill="#fff"/>
      <rect x="565" y="558" width="28" height="14" rx="7" transform="rotate(-45 579 565)"/>
      <path d="M588 553 l5 -5"/>
    </g>
  </svg>

  <div class="brand"><span>Ziegenhof<br>Lindental</span></div>

  <header class="headline">
    <div class="headline__big">Herzlich<br>Willkommen</div>
    <div class="headline__small">auf unserem Hof</div>
  </header>

  <div class="offer" style="left:465px;top:236px">Ziegenrohmilch<small>(Frischkäse, Weichkäse, Schnittkäse)</small></div>
  <div class="offer" style="left:490px;top:354px">Ziegenfleisch</div>
  <div class="offer" style="left:548px;top:462px">Ziegenkäse</div>
  <div class="offer" style="left:638px;top:550px">Wurst</div>

  <section class="intro">
    <p>Wir sind ein landwirtschaftlicher Betrieb mit Ziegen­haltung und Direktvermarktung und einer Hofkäserei in der wir unsere Milch zu handwerklich hergestellten Ziegen­käsen (Frischkäse, Weichkäse, Schnittkäse) verarbeiten.</p>
    <p>In unserem Hofladen gibt es noch weitere Produkte wie <strong>Eier, Obst, Gemüse, Nudeln,</strong> und mehr, von benachbarten Betrieben. Käseproben sind ebenfalls buchbar.</p>
    <p>Wir freuen uns, Sie bald einmal persönlich auf unserem Hof willkommen zu heißen.</p>
    <div class="signature">Ihre Familie Berger</div>
  </section>

  <div class="visit">Besuchen<br>Sie uns!</div>

  <address class="contact" style="font-style:normal">
    <div><svg width="10" height="12" viewBox="0 0 10 12"><path d="M5 0a4.5 4.5 0 0 1 4.5 4.5C9.5 8 5 12 5 12S.5 8 .5 4.5A4.5 4.5 0 0 1 5 0z" fill="#fff"/><circle cx="5" cy="4.5" r="1.7" fill="#333"/></svg><span>Lindenweg 4<br>77000 Musterbach</span></div>
    <div><svg width="11" height="11" viewBox="0 0 11 11"><path d="M2 0.5l2 2.5-1 1.3c.7 1.5 1.7 2.5 3.2 3.2l1.3-1 2.5 2-1.2 1.8C4.5 9.7 1 6.3.2 1.7z" fill="#fff"/></svg><span>07000 - 412</span></div>
    <div><svg width="11" height="9" viewBox="0 0 11 9"><rect x=".5" y=".5" width="10" height="8" fill="#fff"/><path d="M.5 .5l5 4.5 5-4.5" fill="none" stroke="#333"/></svg><span>hallo@ziegenhof-lindental.de</span></div>
  </address>

  <div class="web">www.ziegenhof-lindental.de</div>
</main>
</body>
</html>
```